Coastal Rubdown Oil Co. needs a new label.

This massage oil has been in Australia for over 20 years and needs a new label for its plastic 250ml bottles. The current label (8cm x 8cm) looks old fashioned and so we are looking for something that reflects freedom, relaxation, inspiration. The product is made from sweet almond oil and has different essential oils used to give unique smells. I have seen some lovely abstract vector images. I think we need a clean straight look with bright colours. There are currently six variations to the product. "Weary and Worn Heads, Achy and Spent Frames, Couples Mix, Heather Soak Oil, Unwinding Mix, Uplift Mix" Different coloured labels have been used for each of the blends. I have included photos of existing bottles plus some ideas for the labels.

I would like to use the same font on the name of the brand Bramblewick Acres. If we change the font it may be difficult for existing customers to find our product.

Also just under the name Bramblewick Acres I would like to insert a type of logo (can be the shape of a tear drop or round circle) to say:

Massage Oil
Since 1970

The size of the label is 8cm x 12 cm for the front and the same size for the back of the label.
Updates

Coastal Rubdown oil Company has posted on the brief some images from Pixelvault plus two photos of the original bottles. I am looking for a new design which is bright in colour, fun and funky. I am not thinking along the lines of the traditional Herb and trees look. I think the original label is too busy and the colours overpower the label. The other point I think that is important is that the product has been around since 1970. If there is room I think a round logo which says: Massage Oil Since 1970 I am hoping that we can fit this information on the label Looking forward to seeing all the designs come thru. So far I have only had two designs come thru. Speak soon from hot sunny Australia. maree

Thank you to everyone who has already posted designs for our Massage Label. I have now edited the brief to include some more ideas on how to make this design the Best! I will email back to you straight away ideas and thoughts on your designs. Remember I live in Australia and can be either 10hrs in front or behind your time.

Reason: Due to busy lives and commitments over the next few days I feel that an extension will benefit all involved. Thank you to everyone who has submitted designs and working with me to create something beautiful. maree

Hello from Australia all the designers who have submitted some wonderful designs over the past two weeks. We are now entering the final three days of the competition. Thank you to everyone who has worked so hard to try and create the perfect label for my massage oil bottle. All of you have done a fantastic job. This has made the decision hard to make. Thank you to everyone. Please submit all your last minute designs soon. kind regards maree Australia

Target Market(s)

The type of person purchasing a massage oil blend will buy from a health food shop, pharmacy or from an on-line store. I believe they are wanting something bright that clearly communicates that that it is a massage oil.

Industry/Entity Type

Massage

Font styles to use
Script

Requirements
Must have
• Different colour for each massage oil blend.
Need same font for the name Bramblewick Acres. (script font or similar)

Abstract design please.
Nice to have
• A logo under the name Bramblewick Acres

Tear Drop or circle design that says:

Massage Oil
Since 1970

also we would like an outline for the back label. (see photo attached)

BACK LABEL information

A unique blend of essential oils in a fine light base.

Contains:

vegetable oil extract of nettle, sweet almond oil, ethanol, essential oils of lavender, lemongrass, orange & ylang ylang and vitamin E.

How to Use:

Shake well warm bottle in warm water if very cold.
Lovingly massage the body from head to toe.
Not for medicinal use.

Bramblewick Acres
Hollin WA 6099
Phone: (08) 9555 0142

(LEAVE ROOM FOR BARCODE)
Should not have
• Too busy design or old fashioned design.
No dull colours.

```html
<!DOCTYPE html>
<html lang="en">
<head>
<meta charset="utf-8">
<title>Bramblewick Acres – Massage Oil Label</title>
<link href="https://fonts.googleapis.com/css2?family=Parisienne&family=Raleway:wght@400;600;700&family=Montserrat:wght@600;700&display=swap" rel="stylesheet">
<style>
  :root {
    --canvas-bg: #ebebeb;
    --label-bg: #ffffff;
    --teal-deep: #17587a;
    --cyan: #1bb3d3;
    --pattern-tint: rgba(23, 88, 122, 0.16);
    --pattern-fade: rgba(23, 88, 122, 0);
    --caption: #222222;
    --white: #ffffff;
  }
  * { margin: 0; padding: 0; box-sizing: border-box; }
  html, body { width: 1200px; height: 857px; overflow: hidden; }
  body { background: var(--canvas-bg); font-family: "Raleway", sans-serif; color: var(--teal-deep); }
  .canvas { position: relative; width: 1200px; height: 857px; }

  .label {
    position: absolute; top: 30px; height: 780px;
    background: var(--label-bg); border-radius: 22px; overflow: hidden;
    box-shadow: 0 2px 8px rgba(0,0,0,0.12);
  }
  .label--back { left: 68px; width: 474px; }
  .label--front { left: 612px; width: 520px; }

  .pattern { position: absolute; }
  .pattern--top { left: 0; top: 0; width: 100%; height: 110px;
    background: linear-gradient(180deg, var(--pattern-tint), var(--pattern-fade)); }
  .pattern--left { left: 0; top: 0; width: 70px; height: 100%;
    background: linear-gradient(90deg, var(--pattern-tint), var(--pattern-fade)); }
  .pattern--right { right: -60px; top: 240px; width: 140px; height: 440px;
    background: radial-gradient(ellipse at 100% 50%, rgba(23,88,122,0.2), var(--pattern-fade) 70%); }
  .pattern--bottom { left: 0; bottom: 0; width: 100%; height: 170px;
    background: linear-gradient(0deg, rgba(23,88,122,0.28), var(--pattern-fade)); }
  .pattern--front-top { left: 0; top: 0; width: 100%; height: 100px;
    background: linear-gradient(180deg, rgba(23,88,122,0.18), var(--pattern-fade)); }
  .pattern--front-left { left: 0; top: 0; width: 60px; height: 420px;
    background: linear-gradient(90deg, var(--pattern-tint), var(--pattern-fade)); }
  .meadow { position: absolute; left: 0; bottom: 0; width: 100%; height: 190px;
    background: linear-gradient(0deg, var(--teal-deep) 0%, var(--teal-deep) 30%, rgba(23,88,122,0.35) 70%, var(--pattern-fade) 100%); }

  .badge-mark { position: absolute; border-radius: 50%; background: var(--cyan); }
  .wordmark {
    position: absolute; left: 0; width: 100%; text-align: center; white-space: nowrap;
    font-family: "Parisienne", cursive; font-weight: 400; color: var(--teal-deep); line-height: 1;
  }

  /* back */
  .label--back .badge-mark { left: 204px; top: 112px; width: 66px; height: 66px; }
  .label--back .wordmark--line1 { top: 180px; font-size: 54px; }
  .label--back .wordmark--line2 { top: 240px; font-size: 54px; padding-left: 70px; }
  .back-copy {
    position: absolute; left: 55px; width: 364px; top: 340px;
    font-size: 14.5px; line-height: 1.42; text-align: center;
  }
  .back-copy p + p { margin-top: 9px; }
  .back-copy strong { font-weight: 700; }
  .contact {
    position: absolute; right: 269px; top: 538px; text-align: right; font-style: normal;
    font-size: 14.5px; font-weight: 700; line-height: 1.45;
  }
  .barcode-space {
    position: absolute; left: 217px; top: 526px; width: 153px; height: 87px;
    background: var(--teal-deep); color: var(--white);
    font-size: 15px; font-weight: 700; display: flex; align-items: center; justify-content: center;
  }

  /* front */
  .volume {
    position: absolute; right: 0; top: 96px; width: 138px; height: 48px;
    background: var(--teal-deep); color: var(--white); border-radius: 12px 0 0 12px;
    font-size: 30px; font-weight: 400; text-align: center; line-height: 48px;
  }
  .label--front .badge-mark { left: 212px; top: 118px; width: 112px; height: 112px; }
  .label--front .wordmark--line1 { top: 228px; font-size: 84px; }
  .label--front .wordmark--line2 { top: 322px; font-size: 84px; padding-left: 100px; }
  .headline {
    position: absolute; left: 0; width: 100%; top: 466px; text-align: center;
    font-family: "Montserrat", sans-serif; font-weight: 700; color: var(--teal-deep);
  }
  .headline__lead { display: block; font-size: 29px; line-height: 36px; }
  .headline__name { display: block; font-size: 34px; line-height: 46px; font-weight: 600; }
  .tagline {
    position: absolute; left: 0; width: 100%; top: 553px; text-align: center;
    font-size: 16.5px; font-weight: 600; letter-spacing: 3.2px; color: var(--cyan);
  }

  .caption {
    position: absolute; top: 821px; font-family: "Montserrat", sans-serif;
    font-weight: 700; font-size: 15px; letter-spacing: 1px; color: var(--caption);
    transform: translateX(-50%);
  }
  .caption--back { left: 305px; }
  .caption--front { left: 872px; }
</style>
</head>
<body>
<main class="canvas">
  <section class="label label--back" aria-label="Back label">
    <div class="pattern pattern--top" role="img" aria-label="Abstract blue floral pattern"></div>
    <div class="pattern pattern--left" role="img" aria-label="Abstract blue floral pattern"></div>
    <div class="pattern pattern--right" role="img" aria-label="Abstract blue floral pattern"></div>
    <div class="pattern pattern--bottom" role="img" aria-label="Abstract blue floral pattern"></div>

    <span class="badge-mark" aria-hidden="true"></span>
    <div class="wordmark wordmark--line1">Bramblewick</div>
    <div class="wordmark wordmark--line2">Acres</div>

    <div class="back-copy">
      <p>A unique blend of essential oils in a fine light base.</p>
      <p><strong>Contains:</strong> Vegetable oil extract of nettle, sweet almond oil, ethanol, essential oils of lavender, lemongrass, orange &amp; ylang ylang and vitamin E.</p>
      <p><strong>How to Use:</strong> Shake well warm bottle in warm water if very cold. Lovingly massage the body from head to toe. Not for medicinal use.</p>
    </div>

    <address class="contact">
      Bramblewick Acres<br>
      Hollin WA 6099<br>
      Phone: (08) 9555 0142
    </address>
    <div class="barcode-space">BARCODE</div>
  </section>

  <section class="label label--front" aria-label="Front label">
    <div class="pattern pattern--front-top" role="img" aria-label="Abstract blue floral pattern"></div>
    <div class="pattern pattern--front-left" role="img" aria-label="Abstract blue floral pattern"></div>
    <div class="volume">250 ml</div>

    <span class="badge-mark" aria-hidden="true"></span>
    <div class="wordmark wordmark--line1">Bramblewick</div>
    <div class="wordmark wordmark--line2">Acres</div>

    <h1 class="headline">
      <span class="headline__lead">MASSAGE OIL FOR</span>
      <span class="headline__name">WEARY &amp; WORN HEADS</span>
    </h1>
    <p class="tagline">TWENTY YEARS OF NATURAL SKIN CARE</p>

    <div class="meadow" role="img" aria-label="Silhouette of meadow grass and wildflowers with dragonflies"></div>
  </section>

  <span class="caption caption--back">BACK</span>
  <span class="caption caption--front">FRONT</span>
</main>
</body>
</html>
```